Redesign of Website

We need an overhaul of our website. I've attached our current logo files. Please visit www.pelvorix.com for our current website for information about our company. We are looking for the same type of website (information-based only) so no need for any online store, payments, interactive stuff or anything like that...basically looking for a fresh new look! Also please make sure this design will be mobile-friendly. Thanks!

```html
<!DOCTYPE html>
<html lang="en">
<head>
<meta charset="utf-8">
<title>Pelvorix Consultants, Inc.</title>
<link href="https://fonts.googleapis.com/css2?family=Montserrat:wght@400;500;600;700&family=Open+Sans:wght@400;600&display=swap" rel="stylesheet">
<style>
:root{
  --navy:#0d2a4f;
  --navy-deep:#0a2243;
  --blue:#1e73c8;
  --blue-bright:#2a86e0;
  --sky:#6f9cc8;
  --ink:#1c2a3a;
  --muted:#6b7785;
  --line:#dfe5ec;
  --white:#ffffff;
  --paper:#f4f6f9;
}
*{box-sizing:border-box;margin:0;padding:0}
html,body{width:1200px;height:2800px;overflow:hidden;background:var(--white)}
body{font-family:"Open Sans",Arial,sans-serif;color:var(--ink);position:relative}
h1,h2,h3,h4,.nav,.btn,.logo{font-family:"Montserrat",Arial,sans-serif}
.btn{display:inline-block;background:var(--blue);color:var(--white);font-size:13px;font-weight:600;padding:11px 26px;border-radius:20px;text-decoration:none}

/* header + hero */
.hero{position:absolute;top:0;left:0;width:1200px;height:620px;background:linear-gradient(180deg,#2b3f5c 0%,#5d7594 45%,#8e9fb6 75%,#cfd7e2 100%)}
.hero-photo{position:absolute;inset:0;background:linear-gradient(100deg,rgba(20,34,58,.55) 0%,rgba(20,34,58,.15) 60%,rgba(255,255,255,.05) 100%)}
.site-header{position:absolute;top:0;left:0;width:1200px;height:86px;display:flex;align-items:center;padding:0 80px;z-index:2}
.logo{display:flex;align-items:center;gap:10px;color:var(--white);font-size:22px;font-weight:600;letter-spacing:.3px}
.logo-dot{width:26px;height:26px;border-radius:50%;background:var(--white)}
.nav{display:flex;gap:6px;margin-left:auto;margin-right:36px}
.nav a{color:var(--white);text-decoration:none;font-size:13px;font-weight:500;padding:8px 14px}
.nav a.active{background:var(--blue)}
.call{color:var(--white);font-size:12px;line-height:1.4;margin-right:26px;font-family:"Montserrat",sans-serif}
.call strong{display:block;color:#9cc7f2;font-size:13px}
.hero-copy{position:absolute;left:200px;top:190px;width:560px;z-index:2}
.hero-copy h1{color:var(--white);font-size:30px;line-height:1.35;font-weight:600;margin-bottom:30px}
.dots{position:absolute;right:230px;top:350px;display:flex;gap:8px;z-index:2}
.dots span{width:8px;height:8px;border-radius:50%;background:rgba(255,255,255,.5)}
.dots span:first-child{background:var(--white)}

/* feature cards */
.features{position:absolute;top:480px;left:200px;width:800px;height:250px;background:var(--white);box-shadow:0 10px 30px rgba(10,34,67,.15);display:flex;gap:24px;padding:40px 28px;z-index:3}
.feature{flex:1;background:var(--blue);color:var(--white);padding:70px 18px 18px;position:relative}
.feature.raised{background:var(--blue-bright);margin-top:-16px}
.feature h3{font-size:15px;font-weight:600;margin-bottom:8px}
.feature p{font-size:11px;line-height:1.5;opacity:.9}
.feature .more{font-size:11px;font-weight:600;margin-top:10px;display:block}

/* about */
.about{position:absolute;top:770px;left:0;width:1200px;height:420px}
.about-text{position:absolute;left:200px;top:40px;width:380px}
.eyebrow{color:var(--blue);font-size:13px;font-weight:600;font-family:"Montserrat",sans-serif}
.about h2{font-size:28px;font-weight:700;color:var(--ink);margin:6px 0 18px}
.about p{font-size:12px;line-height:1.75;color:var(--muted);margin-bottom:14px}
.about-photo{position:absolute;right:0;top:0;width:600px;height:420px;background:linear-gradient(135deg,#c9d6e4 0%,#9fb2c7 45%,#d8c6a8 100%)}

/* services */
.services{position:absolute;top:1220px;left:0;width:1200px;height:520px;background:var(--navy);color:var(--white)}
.section-title{text-align:center;font-size:26px;font-weight:600;padding-top:56px}
.section-title + .rule{width:40px;height:2px;background:var(--blue);margin:14px auto 0}
.service-row{position:absolute;top:150px;left:200px;width:800px;display:flex;gap:40px}
.service{flex:1}
.service .icon{width:66px;height:66px;border-radius:50%;border:2px solid var(--blue);display:flex;align-items:center;justify-content:center;margin-bottom:24px}
.service .icon.filled{background:var(--blue)}
.service h3{font-size:15px;font-weight:600;line-height:1.35;margin-bottom:12px}
.service p{font-size:11.5px;line-height:1.6;color:#b9c6d8}
.service .more{display:block;margin-top:16px;font-size:11px;color:var(--white);font-weight:600}
.arrow{position:absolute;top:260px}
.arrow.left{left:150px}
.arrow.right{right:150px}

/* team */
.team{position:absolute;top:1740px;left:0;width:1200px;height:500px;background:var(--white)}
.team .section-title{color:var(--ink)}
.team .sub{text-align:center;font-size:12px;color:var(--muted);margin-top:12px}
.team-row{position:absolute;top:150px;left:110px;width:980px;display:flex;gap:30px}
.member{flex:1;text-align:center}
.member .photo{height:230px;background:linear-gradient(180deg,#e6e8eb 0%,#b9c1cb 55%,#3a4552 100%);margin-bottom:16px}
.member h4{font-size:14px;font-weight:600;color:var(--ink)}
.member span{font-size:11px;color:var(--muted)}

/* contact */
.contact{position:absolute;top:2240px;left:0;width:1200px;height:490px;background:var(--navy-deep);color:var(--white)}
.contact-info{position:absolute;left:200px;top:60px;width:260px}
.contact h2{font-size:24px;font-weight:600;margin-bottom:22px}
.contact-info p{font-size:12px;line-height:1.8;color:#c6d2e2}
.contact-info .phone{color:#9cc7f2}
.socials{display:flex;gap:10px;margin-top:22px}
.socials span{width:28px;height:28px;background:#1c3a63;border-radius:3px}
.callback{position:absolute;left:480px;top:60px;width:520px}
.fields{display:flex;gap:12px;margin-bottom:12px}
.field{flex:1;height:34px;border:1px solid #3b5a82;font-size:11px;color:#8ea3bf;padding:9px 10px}
.field.message{height:110px}
.callback .btn{margin-top:16px;border-radius:18px;padding:10px 28px}

/* footer */
.site-footer{position:absolute;top:2730px;left:0;width:1200px;height:70px;background:var(--white);display:flex;align-items:center;padding:0 200px;font-size:11px;color:var(--muted)}
.footer-links{margin-left:auto;margin-right:30px;display:flex;gap:14px}
.footer-links a{color:var(--muted);text-decoration:none}
.site-footer .btn{font-size:11px;padding:9px 20px}
</style>
</head>
<body>

<section class="hero">
  <div class="hero-photo" role="img" aria-label="City skyline with construction cranes at dusk"></div>
  <header class="site-header">
    <div class="logo"><span class="logo-dot"></span>Pelvorix Consultants, Inc.</div>
    <nav class="nav"><a class="active" href="#">Home</a><a href="#">About</a><a href="#">Services</a><a href="#">Contact</a></nav>
    <div class="call">Call Us Today!<strong>(555) 014-2290</strong></div>
    <a class="btn" href="#">Get Free Quotes</a>
  </header>
  <div class="hero-copy">
    <h1>Pelvorix provides our clients with in-depth plan &amp; cost, construction funding, environmental and property condition reports.</h1>
    <a class="btn" href="#">Contact Us Today</a>
  </div>
  <div class="dots"><span></span><span></span><span></span></div>
</section>

<section class="features">
  <div class="feature">
    <h3>We Innovate</h3>
    <p>We deliver fresh perspectives on every project we review.</p>
  </div>
  <div class="feature raised">
    <h3>Performance</h3>
    <p>We deliver fast, precise reports for our lenders and owners.</p>
    <span class="more">&#8594; Read More</span>
  </div>
  <div class="feature">
    <h3>A Full Service</h3>
    <p>One firm for planning, funding, inspection and condition review.</p>
  </div>
</section>

<section class="about">
  <div class="about-text">
    <div class="eyebrow">www.pelvorix.com</div>
    <h2>Pelvorix Consultants, Inc.</h2>
    <p>With over 30 years of experience, we provide consultants and comprehensive inspection services to financial institutions involved in construction and loan management in the region and beyond.</p>
    <p>Our professional staff bring years of engineering, environmental, building and real estate experience to serve lenders, owners, investors and developers on projects of every size.</p>
    <a class="btn" href="#">About Us</a>
  </div>
  <div class="about-photo" role="img" aria-label="Engineer in a hard hat reviewing plans with a couple beside a house under construction"></div>
</section>

<section class="services">
  <h2 class="section-title">Service We Offers</h2>
  <div class="rule"></div>
  <svg class="arrow left" width="14" height="24" viewBox="0 0 14 24"><path d="M12 2 2 12l10 10" fill="none" stroke="#fff" stroke-width="2"/></svg>
  <svg class="arrow right" width="14" height="24" viewBox="0 0 14 24"><path d="M2 2l10 10L2 22" fill="none" stroke="#fff" stroke-width="2"/></svg>
  <div class="service-row">
    <div class="service">
      <div class="icon filled"><svg width="28" height="32" viewBox="0 0 28 32"><rect x="3" y="2" width="22" height="28" rx="2" fill="none" stroke="#fff" stroke-width="2"/><path d="M8 10h12M8 16h12M8 22h8" stroke="#fff" stroke-width="2"/></svg></div>
      <h3>Property Condition Reports</h3>
      <p>We will provide you with a report that includes digital photographs and estimated costs for any immediate repairs needed.</p>
      <span class="more">&#8594; Read More</span>
    </div>
    <div class="service">
      <div class="icon"><svg width="30" height="30" viewBox="0 0 30 30"><rect x="3" y="5" width="24" height="20" fill="none" stroke="#2a86e0" stroke-width="2"/><path d="M3 11h24M10 5v20" stroke="#2a86e0" stroke-width="2"/></svg></div>
      <h3>Plan and Cost Reviews</h3>
      <p>Our plan and cost reviews provide lending institutions with expert study of new construction projects before loan commitment.</p>
      <span class="more">&#8594; Read More</span>
    </div>
    <div class="service">
      <div class="icon"><svg width="30" height="30" viewBox="0 0 30 30"><path d="M4 26V12l11-8 11 8v14z" fill="none" stroke="#2a86e0" stroke-width="2"/><path d="M12 26v-8h6v8" fill="none" stroke="#2a86e0" stroke-width="2"/></svg></div>
      <h3>Construction Funding Inspections</h3>
      <p>Lending institutions rely on our inspectors to evaluate multiple stages of new construction and release funds safely.</p>
      <span class="more">&#8594; Read More</span>
    </div>
  </div>
</section>

<section class="team">
  <h2 class="section-title">Our Team</h2>
  <p class="sub">Members of Organizations &amp; Varying Phases of Construction</p>
  <div class="team-row">
    <div class="member"><div class="photo" role="img" aria-label="Portrait of team member in suit"></div><h4>Owen Halvers</h4><span>President</span></div>
    <div class="member"><div class="photo" role="img" aria-label="Portrait of team member in suit"></div><h4>Rhea Castellan</h4><span>Vice President</span></div>
    <div class="member"><div class="photo" role="img" aria-label="Portrait of team member in suit"></div><h4>Mira Dovenko</h4><span>Director of Operations</span></div>
    <div class="member"><div class="photo" role="img" aria-label="Portrait of team member in suit"></div><h4>Tobin Ashgrove</h4><span>Project Construction Manager</span></div>
  </div>
</section>

<section class="contact">
  <div class="contact-info">
    <h2>Contact Info</h2>
    <p class="phone">(555) 014-2290</p>
    <p>info@pelvorix.com</p>
    <p>48 Larkfield Rd<br>Brenmoor, ST 00412</p>
    <div class="socials"><span></span><span></span><span></span></div>
  </div>
  <div class="callback">
    <h2>Request a Call Back.</h2>
    <div class="fields"><div class="field">Your Name</div><div class="field">Email</div><div class="field">Phone</div></div>
    <div class="field message">Message</div>
    <a class="btn" href="#">Submit</a>
  </div>
</section>

<footer class="site-footer">
  <span>Copyright 2018 · Pelvorix</span>
  <div class="footer-links"><a href="#">Home</a><a href="#">About</a><a href="#">Services</a><a href="#">Contact</a></div>
  <a class="btn" href="#">Get Free Quotes</a>
</footer>

</body>
</html>
```